Web-page design

We need a initial web design for our page kavilora.com.au (which is not yet set up).
We provide consulting services for all kinds of problems in and between organisations.
Main focus is on conflict resolution but we also support companies on improving their operational performance.
We want to have the following page structure (and part of the project is to design the 8 pages):
- Home
- Services (we offer 3 main service areas - one per page)
- Case studies (one per page)
- Engaging us (our process)
- About Conflict & low performance
- Conflict resolution App
- About
- Contact (Email form)
- Our logo should be on each page.
The start page should include the following information:
- Twitter / Linkedin / facebook/ google + Links
- Telephone / Email or in general contact details
- News
- A quite prominent picture box with 3 alternating pics - each representing one of our service areas
- Link to our App
- Testimonials
It would be nice if the service pages would have an image header. Links to the information section (about conflict & low performance; and the app page) would be nice as well.
We like the following joomla designs: www.quorbixlane.com/itempreview/153
No need to copy it, it should just give you an idea.
We like the layout here with the picture and space for the case studies on the left. Somewhere beneath should be the 3 service areas with a picture each.
In terms of colors: our logo colours are Blue (RBG 8;44;80) and Orange (RGB 231;120;23). The orange could be used to emphasise certain things, however there should not be too much color.
Budget for images available, so please use placeholders or ask us for specific photos/images, if you need them for your design.
Updates
Hi, one more thing that we would like to have is the case studies not hidden behind a link "case studies" - we would like to have them individually linked prominent on the first page. There will be about 6-8 of them. Thats what we liked on the joomla template (the links left from the picture).
Hi, thanks very much for all the great proposals.
We are currently going through the selection process and will post our decision early next week.
Thanks again!
Liesel
Target Market(s)
- target customers are all different kinds of businesses and organisations (all industries, government, non-for-profit, ...) experiencing conflict and tension - be it with internal staff, amongst managers or board members, dysfunctional teams, between organizations or customers and organizations... examples could be bullying allegations, governmental negotiations with unions, disputes within organizations etc.
- also we will offer performance improvement services for organizations
- we will offer mediation, facilitation, negotiation, performance improvement services, conflict coaching, conflict management, change management services
- if comparable to anything - then to a law firm in terms of dealing with conflicts but its much less adversarial and much more about the people and their interests rather than about laws
- basically it's all kind of things you can do in order to solve disputes without involving lawyers and a court - so it's much cheaper and target is to find a solution all parties can live with rather than having a judge deciding about who wins and who looses
- performance management is more about analysing reasons for a lack of performance and setting up continous improvement systems, supporting change management, facilitating improvement workshops or strategic meetings, ...
Industry/Entity Type
Consulting
Look and feel

```html
<!DOCTYPE html>
<html lang="en">
<head>
<meta charset="utf-8">
<title>Kavilora – Conflict Resolution &amp; Performance</title>
<link href="https://fonts.googleapis.com/css2?family=Open+Sans:ital,wght@0,400;0,600;0,700;1,400&family=Didact+Gothic&display=swap" rel="stylesheet">
<style>
:root{
  --navy:#082c50;
  --orange:#e77817;
  --paper:#e4e4e4;
  --paper-dark:#d2d2d2;
  --white:#ffffff;
  --text:#0d2a4a;
  --tile-red:#d34836;
  --tile-blue:#0e76a8;
  --tile-indigo:#3b5998;
  --tile-sky:#1da1f2;
}
*{margin:0;padding:0;box-sizing:border-box}
html,body{width:988px;height:1200px;overflow:hidden;background:var(--white)}
body{position:relative;font-family:"Open Sans",Arial,sans-serif;color:var(--text)}
a{color:inherit}
.abs{position:absolute}

/* header */
.site-header{position:absolute;left:0;top:0;width:988px;height:95px;background:linear-gradient(180deg,#efefef,#dcdcdc);border-bottom:2px solid #cfcfcf}
.header-accent{position:absolute;left:0;top:0}
.brand{position:absolute;left:48px;top:24px;display:flex;align-items:center;gap:12px}
.brand-mark{width:22px;height:22px;border:3px solid var(--navy)}
.brand-name{font-size:34px;font-weight:400;letter-spacing:1px;color:var(--navy)}
.brand-url{position:absolute;left:75px;top:70px;font-size:13px;font-weight:600;letter-spacing:7.5px;color:var(--navy)}
.main-nav{position:absolute;top:11px;left:575px;display:flex;font-weight:700;font-size:16px}
.main-nav a{text-decoration:none;color:var(--navy)}
.main-nav a.current{color:var(--white)}
.nav-home{margin-right:54px}.nav-services{margin-right:48px}.nav-about{margin-right:44px}
.contact-line{position:absolute;right:27px;top:47px;text-align:right;font-size:12px;font-weight:700;line-height:17px;color:var(--navy)}

/* social */
.social{position:absolute;left:0;top:173px;width:44px}
.social span{display:flex;align-items:center;justify-content:center;height:45.5px}
.social i{display:block;width:14px;height:14px;border-radius:50%;background:var(--white)}

/* quick links note */
.quick-links{position:absolute;left:57px;top:125px;width:247px;height:186px;background:linear-gradient(135deg,#ececec,#dadada);box-shadow:-3px 3px 6px rgba(0,0,0,.35);padding:24px 0 0 8px}
.quick-links li{list-style:none;display:flex;align-items:flex-start;font-weight:700;font-size:15px;line-height:21px;margin-bottom:25px}
.quick-links li:nth-child(2){margin-bottom:24px}
.arrow{display:inline-block;width:0;height:0;border-left:15px solid var(--orange);border-top:8px solid transparent;border-bottom:8px solid transparent;margin:3px 10px 0 0;flex:none}

/* services */
.photo{position:absolute;border-radius:50%}
.col-title{position:absolute;text-align:center;font-weight:700;font-size:15px;line-height:21px}
.news-label{position:absolute;left:62px;top:338px;font-style:italic;color:var(--orange);font-size:15px}
.copy{position:absolute;font-weight:700;font-size:14.6px;line-height:20.8px;width:200px}
.more{color:var(--orange);font-weight:700}

.bar{position:absolute}
.navy{background:var(--navy)}.orange{background:var(--orange)}

/* case studies */
.section-title{position:absolute;font-family:"Didact Gothic",sans-serif;font-weight:700;font-size:22px;letter-spacing:5px;color:var(--navy);-webkit-text-stroke:.6px var(--navy)}
.case{position:absolute;width:260px;height:38px;background:linear-gradient(180deg,#ebebeb,#dcdcdc);box-shadow:-3px 2px 5px rgba(0,0,0,.35);display:flex;align-items:center;padding-left:9px;font-weight:700;font-size:15px}
.case .arrow{margin:0 13px 0 0}
.deco-square{position:absolute;left:789px;top:744px;width:32px;height:32px;border:3px solid var(--navy);transform:rotate(45deg)}

/* testimonials */
.quote-name{position:absolute;font-weight:600;font-size:15px}
.quote{position:absolute;width:262px;font-style:italic;font-size:14.6px;line-height:21px}
.copyright{position:absolute;left:60px;top:1117px;font-size:11.5px;letter-spacing:.3px}
</style>
</head>
<body>

<header class="site-header">
  <svg class="header-accent" width="988" height="95" aria-hidden="true"><polygon points="545,0 988,0 988,95 450,95" fill="#e77817"/></svg>
  <div class="brand"><span class="brand-mark"></span><span class="brand-name">KAVILORA</span></div>
  <div class="brand-url">www.kavilora.com.au</div>
  <nav class="main-nav">
    <a class="nav-home current" href="#">HOME</a>
    <a class="nav-services" href="#">SERVICES</a>
    <a class="nav-about" href="#">ABOUT</a>
    <a href="#">CONTACT</a>
  </nav>
  <div class="contact-line">call us: + 000 000<br>hello@kavilora.com.au</div>
</header>

<div class="social" aria-label="Social links">
  <span style="background:var(--tile-red)"><i></i></span>
  <span style="background:var(--tile-blue)"><i></i></span>
  <span style="background:var(--tile-indigo)"><i></i></span>
  <span style="background:var(--tile-sky)"><i></i></span>
</div>

<ul class="quick-links">
  <li><span class="arrow"></span><a href="#">CONFLICT RESOLUTION APP</a></li>
  <li><span class="arrow"></span><a href="#">SOLVE CONFLICTS<br>&nbsp;&amp; LOW PERFORMANCE</a></li>
  <li><span class="arrow"></span><a href="#" style="margin-left:3px">CONTACT US</a></li>
</ul>

<div class="photo" role="img" aria-label="Photo of business people shaking hands" style="left:338px;top:122px;width:200px;height:200px;background:radial-gradient(circle at 45% 40%,#8a8f96,#2c2f35)"></div>
<div class="photo" role="img" aria-label="Photo of medical staff working at a computer" style="left:557px;top:121px;width:200px;height:198px;background:radial-gradient(circle at 50% 45%,#c7d4e2,#4d6f93)"></div>
<div class="photo" role="img" aria-label="Photo of two people meditating" style="left:772px;top:128px;width:196px;height:194px;background:radial-gradient(circle at 50% 45%,#e4e8ef,#2f4a72)"></div>

<div class="news-label">NEWS</div>
<p class="copy" style="left:59px;top:376px;width:220px">&nbsp;Proin gravida nibh vel velit auctor aliquet. Aenean sollicitudin, lorem quis bibendum auctor, nisi elit consequat ipsum, nec sagittis sem nibh id. <a class="more" href="#">READ MORE</a></p>

<div class="col-title" style="left:340px;top:343px;width:170px">SOLVE CONFLICTS</div>
<p class="copy" style="left:333px;top:378px">Proin gravida nibh vel velit auctor aliquet. Aenean sollicitudin, lorem quis bibendum auctor, nisi elit consequat ipsum, nec sagitti. <a class="more" href="#">READ MORE</a></p>

<div class="col-title" style="left:568px;top:325px;width:170px">IMPROVE<br>PERFORMANCE</div>
<p class="copy" style="left:559px;top:376px">Proin gravida nibh vel velit auctor aliquet. Aenean sollicitudin, lorem quis bibendum auctor, nisi elit consequat ipsum, nec sagitti. <a class="more" href="#">READ MORE</a></p>

<div class="col-title" style="left:776px;top:341px;width:170px">SELF GROWTH</div>
<p class="copy" style="left:772px;top:376px;width:198px">Proin gravida nibh vel velit auctor aliquet. Aenean sollicitudin, lorem quis bibendum auctor, nisi elit consequat ipsum, nec sagitti. <a class="more" href="#">READ MORE</a></p>

<div class="bar orange" style="left:303px;top:435px;width:5px;height:112px"></div>
<div class="bar navy" style="left:303px;top:542px;width:105px;height:6px"></div>
<div class="bar navy" style="left:978px;top:441px;width:6px;height:107px"></div>
<div class="bar orange" style="left:873px;top:542px;width:111px;height:6px"></div>

<h2 class="section-title" style="left:302px;top:568px">CASE STUDIES</h2>

<a class="case" href="#" style="left:55px;top:632px"><span class="arrow"></span><u>CASE STUDY</u></a>
<a class="case" href="#" style="left:55px;top:674px"><span class="arrow"></span><u>CASE STUDY</u></a>
<a class="case" href="#" style="left:55px;top:719px"><span class="arrow"></span><u>CASE STUDY</u></a>
<a class="case" href="#" style="left:366px;top:632px"><span class="arrow"></span><u>CASE STUDY</u></a>
<a class="case" href="#" style="left:366px;top:674px"><span class="arrow"></span><u>CASE STUDY</u></a>
<a class="case" href="#" style="left:366px;top:719px"><span class="arrow"></span><u>CASE STUDY</u></a>
<a class="case" href="#" style="left:677px;top:632px"><span class="arrow"></span><u>CASE STUDY</u></a>
<a class="case" href="#" style="left:677px;top:674px"><span class="arrow"></span><u>CASE STUDY</u></a>
<div class="deco-square" aria-hidden="true"></div>

<div class="bar orange" style="left:0;top:820px;width:988px;height:8px"></div>

<h2 class="section-title" style="left:303px;top:842px">TESTIMONIALS</h2>

<div class="photo" role="img" aria-label="Portrait of a smiling support agent with headset" style="left:67px;top:860px;width:101px;height:101px;background:radial-gradient(circle at 50% 45%,#f0dccb,#9a8577)"></div>
<div class="quote-name" style="left:194px;top:902px">John Doe</div>
<p class="quote" style="left:194px;top:930px">“Proin gravida nibh vel velit auctor aliquet. Aenean sollicitudin, lorem quis bibendum auctor, nisi elit consequat ipsum, nec sagittis sem nibh id.”</p>

<div class="photo" role="img" aria-label="Portrait of a smiling support agent with headset" style="left:562px;top:860px;width:101px;height:101px;background:radial-gradient(circle at 50% 45%,#f0dccb,#9a8577)"></div>
<div class="quote-name" style="left:690px;top:902px">John Doe</div>
<p class="quote" style="left:690px;top:930px">“Proin gravida nibh vel velit auctor aliquet. Aenean sollicitudin, lorem quis bibendum auctor, nisi elit consequat ipsum, nec sagittis sem nibh id.”</p>

<div class="bar navy" style="left:455px;top:967px;width:6px;height:105px"></div>
<div class="bar orange" style="left:349px;top:1065px;width:112px;height:6px"></div>
<div class="bar orange" style="left:551px;top:960px;width:6px;height:106px"></div>
<div class="bar navy" style="left:551px;top:1065px;width:105px;height:6px"></div>

<div class="bar navy" style="left:0;top:1087px;width:988px;height:8px"></div>
<footer class="copyright">COPYRIGHT ©KAVILORA2013. ALL RIGHTS RESERVED</footer>

</body>
</html>
```